Cigar Ring Design

we are working on a project, which is an eCommerce store for cigars, now instead of selling all kind of existing brands this project is based on a TabacoMillDepot concept where an outlet is linked to an actual Cigar factory,
so the cigar lines sold will come out under a TMD (TabacoMillDepot) brand consisting of various labels, (think Barney Cotter, Ochre Crest, Slate Crest etc) I had an idea for the Cigar Rings for this project, where I put TM in an O (circle) of which I made mock ups (see attachement), now I am not a designer, I am sure a real designer can come up with something more stylish and unique.

```html
<!DOCTYPE html>
<html lang="en">
<head>
<meta charset="utf-8">
<title>TabacoMillDepot Cigar Ring</title>
<link rel="stylesheet" href="https://fonts.googleapis.com/css2?family=Josefin+Sans:wght@700&display=swap">
<style>
  :root {
    --backdrop: #f1ede8;
    --band-black: #231f20;
    --ring-gold: #c9a13f;
  }
  html, body {
    margin: 0;
    padding: 0;
    width: 734px;
    height: 1200px;
    overflow: hidden;
    background: var(--backdrop);
  }
  .canvas {
    display: block;
    width: 734px;
    height: 1200px;
  }
  .ring-band,
  .ring-badge {
    fill: var(--band-black);
  }
  .brand-name {
    fill: var(--ring-gold);
    font-family: "Josefin Sans", sans-serif;
    font-weight: 700;
  }
  .badge-name {
    letter-spacing: 1px;
  }
  .mark-circle {
    fill: none;
    stroke: var(--ring-gold);
    stroke-width: 3;
  }
</style>
</head>
<body>
<svg class="canvas" viewBox="0 0 734 1200" xmlns="http://www.w3.org/2000/svg" aria-label="Flat cigar ring band">
  <!-- band strip, rounded at the closing end -->
  <path class="ring-band" d="M23 556 H665 A44 44 0 0 1 665 644 H23 Z"/>

  <!-- scalloped central badge -->
  <g class="ring-badge">
    <circle cx="350" cy="600" r="78"/>
    <circle cx="426" cy="600" r="14"/>
    <circle cx="415.8" cy="638" r="14"/>
    <circle cx="388" cy="665.8" r="14"/>
    <circle cx="350" cy="676" r="14"/>
    <circle cx="312" cy="665.8" r="14"/>
    <circle cx="284.2" cy="638" r="14"/>
    <circle cx="274" cy="600" r="14"/>
    <circle cx="284.2" cy="562" r="14"/>
    <circle cx="312" cy="534.2" r="14"/>
    <circle cx="350" cy="524" r="14"/>
    <circle cx="388" cy="534.2" r="14"/>
    <circle cx="415.8" cy="562" r="14"/>
  </g>

  <!-- badge contents -->
  <circle class="mark-circle" cx="350" cy="582" r="42"/>
  <text class="brand-name" x="350" y="594" font-size="32" text-anchor="middle">TM</text>
  <text class="brand-name badge-name" x="350" y="648" font-size="13" text-anchor="middle">TabacoMillDepot</text>

  <!-- closing-end mark -->
  <circle class="mark-circle" cx="667" cy="600" r="36"/>
  <text class="brand-name" x="667" y="611" font-size="28" text-anchor="middle">TM</text>
</svg>
</body>
</html>
```